Psychology practice - information brochure/flyer - half A4 page folded (4 sides)

We need a brochure/flyer to market our psychology service to GPs (Doctors). We need to demonstrate to the doctors that we are the right choice for their patients, and that we cover a large range of services so all of their patients needs are met. We will demonstrate this by listing our range of services and our team of psychologists. We have two locations in Sydney and offer high end services. I've attached our company logo but we remain flexible regarding the style of the brochures. I will provide more details (services, locations & psychologist credentials) once our preferred brochure design has been selected.

```html
<!DOCTYPE html>
<html lang="en">
<head>
<meta charset="utf-8">
<title>Psychology Practice – GP Brochure</title>
<link rel="stylesheet" href="https://fonts.googleapis.com/css2?family=Open+Sans:wght@300;400;600;700&display=swap">
<style>
  :root {
    --blue: #14a8f5;
    --pink: #f22e9d;
    --green: #1ecf55;
    --yellow: #ffc517;
    --white: #ffffff;
    --ink: #0d0d0d;
    --rule: #222222;
    --shadow: 0 0 20px 3px rgba(0,0,0,0.72);
    --shadow-soft: 0 0 16px 2px rgba(0,0,0,0.6);
  }
  * { box-sizing: border-box; margin: 0; padding: 0; }
  html, body { width: 1200px; height: 848px; overflow: hidden; background: var(--white); }
  body { font-family: "Open Sans", sans-serif; color: var(--ink); }

  .brochure { position: relative; width: 1200px; height: 848px; overflow: hidden; background: var(--white); }

  .fold-line { position: absolute; left: 606px; top: 0; width: 1px; height: 848px; background: var(--rule); z-index: 6; }

  .accent-column { position: absolute; left: 1004px; top: 0; width: 196px; height: 689px; background: var(--blue); box-shadow: var(--shadow); }

  .footer-band { position: absolute; left: 0; top: 689px; width: 1200px; height: 159px; background: var(--green); box-shadow: 0 -6px 18px 2px rgba(0,0,0,0.7); z-index: 3; }
  .footer-band__title { position: absolute; left: 0; width: 606px; top: 52px; text-align: center; color: var(--white); font-weight: 600; font-size: 36px; line-height: 1.2; }

  .services-panel { position: absolute; left: 64px; top: 83px; width: 494px; height: 620px; border: 8px solid var(--pink); background: var(--white); box-shadow: var(--shadow); z-index: 2; }
  .services-panel__intro { position: absolute; left: 31px; top: 44px; width: 440px; font-weight: 600; font-size: 23px; line-height: 32px; }
  .services-list { position: absolute; left: 31px; top: 172px; list-style: none; }
  .services-list li { position: relative; padding-left: 32px; font-weight: 600; font-size: 29px; line-height: 40.4px; }
  .services-list li::before { content: ""; position: absolute; left: 7px; top: 13px; width: 16px; height: 16px; border-radius: 50%; background: var(--blue); }

  .section-label { position: absolute; color: var(--white); font-weight: 600; display: flex; align-items: center; justify-content: center; box-shadow: var(--shadow); z-index: 4; }
  .section-label--services { left: 29px; top: 40px; width: 395px; height: 86px; background: var(--blue); font-size: 46px; }
  .section-label--about { left: 915px; top: 16px; width: 231px; height: 51px; background: var(--pink); font-size: 32px; box-shadow: var(--shadow-soft); }

  .team-card { position: absolute; left: 634px; width: 541px; height: 182px; border: 10px solid var(--yellow); border-radius: 6px; background: var(--white); box-shadow: var(--shadow-soft); z-index: 5; }
  .team-card--1 { top: 80px; }
  .team-card--2 { top: 267px; }
  .team-card--3 { top: 454px; }
  .team-card--4 { top: 641px; }
  .team-card__name { position: absolute; left: 6px; top: 2px; font-weight: 600; font-size: 30px; line-height: 1.2; }
  .team-card__details { position: absolute; left: 10px; top: 40px; list-style: none; }
  .team-card__details li { position: relative; padding-left: 17px; font-weight: 300; font-size: 16px; height: 36px; line-height: 20px; }
  .team-card__details li::before { content: ""; position: absolute; left: 2px; top: 7px; width: 8px; height: 8px; border-radius: 50%; }
  .team-card__details .detail--qualifications::before { background: var(--blue); }
  .team-card__details .detail--experience::before { background: var(--green); }
  .team-card__details .detail--approach::before { background: var(--pink); }
</style>
</head>
<body>
<main class="brochure">
  <div class="accent-column"></div>

  <section class="services-panel">
    <p class="services-panel__intro">Our specialists have experience working with adults and adolescents seeking assistance with:</p>
    <ul class="services-list">
      <li>Service A</li>
      <li>Service B</li>
      <li>Service C</li>
      <li>Service D</li>
      <li>Service E</li>
      <li>Service F</li>
      <li>Service G</li>
      <li>Service H</li>
      <li>Service I</li>
    </ul>
  </section>
  <h2 class="section-label section-label--services">Our Services</h2>

  <footer class="footer-band">
    <p class="footer-band__title">Evidence Based Treatments</p>
  </footer>

  <h2 class="section-label section-label--about">About Us</h2>

  <article class="team-card team-card--1">
    <h3 class="team-card__name">Name Here</h3>
    <ul class="team-card__details">
      <li class="detail--qualifications">Qualifications - Info here</li>
      <li class="detail--experience">Experience - Info here</li>
      <li class="detail--approach">Approach - Info here</li>
    </ul>
  </article>
  <article class="team-card team-card--2">
    <h3 class="team-card__name">Name Here</h3>
    <ul class="team-card__details">
      <li class="detail--qualifications">Qualifications - Info here</li>
      <li class="detail--experience">Experience - Info here</li>
      <li class="detail--approach">Approach - Info here</li>
    </ul>
  </article>
  <article class="team-card team-card--3">
    <h3 class="team-card__name">Name Here</h3>
    <ul class="team-card__details">
      <li class="detail--qualifications">Qualifications - Info here</li>
      <li class="detail--experience">Experience - Info here</li>
      <li class="detail--approach">Approach - Info here</li>
    </ul>
  </article>
  <article class="team-card team-card--4">
    <h3 class="team-card__name">Name Here</h3>
    <ul class="team-card__details">
      <li class="detail--qualifications">Qualifications - Info here</li>
      <li class="detail--experience">Experience - Info here</li>
      <li class="detail--approach">Approach - Info here</li>
    </ul>
  </article>

  <div class="fold-line"></div>
</main>
</body>
</html>
```